Web Design Project - Quillmore Analytics

I am a Mechanical Engineer running a one person consulting firm at this point. The hope is to expand in the future, but for now I simply need a website that conveys a professional appearance, and allows potential and existing clients to find me. Website design displaying contact information, CV for download, capabilities, past projects, etc. I've included four examples below from companies that provided the same service. I've only provided these as general reference for the type of work I do and how others have chosen to display this information. The design is completely at your discretion.

I've included the current Logo in the uploaded files section. I will provide content as requried.

http://www.torvanmech.com/
http://www.halberic.com/
http://www.rumblaxsystems.com/
http://dorwickmotive.net/

Industry/Entity Type

Consulting

```html
<!DOCTYPE html>
<html lang="en">
<head>
<meta charset="utf-8">
<title>Quillmore Analytics — Engineering Consultants</title>
<link rel="stylesheet" href="https://fonts.googleapis.com/css2?family=Bebas+Neue&family=Josefin+Sans:wght@400;700&family=Arimo:wght@400&display=swap">
<style>
  :root {
    --red-orange: #f0562a;
    --orange: #f28a25;
    --heading-orange: #f0892a;
    --ink: #2b2b2b;
    --white: #ffffff;
    --nav-dark: #1f2440;
    --nav-light: #6d7fae;
    --rule: #e3e3e3;
  }
  * { box-sizing: border-box; margin: 0; padding: 0; }
  html, body { width: 1200px; height: 1142px; overflow: hidden; background: var(--white); }
  body { font-family: "Arimo", Arial, sans-serif; color: var(--ink); position: relative; }

  .hero {
    position: absolute; left: 0; top: 0; width: 1200px; height: 610px;
  }
  .hero-backdrop {
    position: absolute; inset: 0;
    background:
      radial-gradient(circle at 30% 12%, rgba(200,170,150,.45), transparent 22%),
      radial-gradient(circle at 22% 70%, rgba(190,150,120,.4), transparent 20%),
      radial-gradient(circle at 96% 30%, rgba(150,120,140,.45), transparent 22%),
      radial-gradient(circle at 90% 82%, rgba(210,180,150,.35), transparent 20%),
      linear-gradient(135deg, #2c2435 0%, #3a2f3d 45%, #2a2436 100%);
  }

  .brand {
    position: absolute; left: 46px; top: 0; width: 307px; height: 98px;
    background: var(--white);
    display: flex; align-items: center; justify-content: center; gap: 10px;
  }
  .brand-mark { width: 16px; height: 16px; background: var(--orange); }
  .brand-name {
    font-family: "Josefin Sans", sans-serif; font-weight: 700;
    font-size: 22px; letter-spacing: 1.5px; color: var(--orange); text-transform: uppercase;
  }

  .intro {
    position: absolute; right: 439px; top: 68px; width: 460px; text-align: right; color: var(--white);
  }
  .intro-title {
    font-family: "Bebas Neue", sans-serif; font-weight: 400; font-size: 40px; line-height: 44px; letter-spacing: .5px;
  }
  .intro-text { margin-top: 8px; font-size: 14.5px; line-height: 18.5px; }

  .tile {
    position: absolute; width: 185.6px; height: 185.6px;
  }
  .tile--link {
    display: flex; flex-direction: column; align-items: center; justify-content: center;
    gap: 14px; color: var(--white); text-decoration: none; font-size: 19px;
  }
  .tile--red { background: var(--red-orange); }
  .tile--orange { background: var(--orange); }
  .tile svg { width: 60px; height: 60px; }

  .photo-lounge { background: linear-gradient(160deg, #e6e6e6 0%, #9c9c9c 45%, #3f4446 100%); }
  .photo-terrace { background: linear-gradient(180deg, #6a7fa8 0%, #4b4f5e 40%, #c48a48 70%, #5a3d26 100%); }
  .photo-dining { background: linear-gradient(160deg, #7a6048 0%, #a89378 50%, #4b3a2c 100%); }
  .photo-sofa { background: linear-gradient(180deg, #2f3030 0%, #5c5c5c 50%, #1c1c1c 80%, #8a8a8a 100%); }
  .photo-sunset { background: linear-gradient(180deg, #8aa2b8 0%, #d8b060 45%, #4a6a88 75%, #e8e8e8 100%); }
  .photo-living { background: linear-gradient(170deg, #3c4046 0%, #6a6a6c 45%, #b08a3a 65%, #2e2e30 100%); }

  .main-nav {
    position: absolute; left: 0; top: 610px; width: 1200px; height: 48px;
    background: linear-gradient(90deg, var(--nav-dark) 0%, #2a3156 55%, var(--nav-light) 100%);
    border-bottom: 2px solid #9aa4c4;
    display: flex; align-items: center; justify-content: center; gap: 64px; padding-right: 40px;
  }
  .nav-item { display: flex; align-items: center; gap: 14px; color: var(--white); text-decoration: none; font-size: 15.5px; }
  .nav-item svg { width: 30px; height: 30px; }

  .solutions { position: absolute; left: 0; top: 712px; width: 1200px; text-align: center; }
  .solutions-title {
    font-family: "Josefin Sans", sans-serif; font-weight: 700; font-size: 45px; line-height: 50px;
    color: var(--heading-orange); letter-spacing: 1.5px; text-transform: uppercase;
  }
  .solutions-lead {
    font-family: "Josefin Sans", sans-serif; font-weight: 400; font-size: 24px; line-height: 29px;
    color: var(--ink); letter-spacing: 1px; text-transform: uppercase; margin-top: 2px;
  }

  .rule { position: absolute; left: 48px; top: 878px; width: 1112px; height: 1px; background: var(--rule); }

  .capability { position: absolute; top: 914px; width: 360px; text-align: center; }
  .capability svg { width: 72px; height: 72px; }
  .capability-title {
    font-family: "Bebas Neue", sans-serif; font-weight: 400; font-size: 36px; line-height: 40px;
    color: var(--ink); margin-top: 32px;
  }
  .capability-text { font-size: 17.5px; line-height: 19.5px; color: #333; margin-top: 16px; }
</style>
</head>
<body>

<header class="hero">
  <div class="hero-backdrop" role="img" aria-label="Softly blurred interior backdrop with warm bokeh lights"></div>

  <div class="brand">
    <span class="brand-mark"></span>
    <span class="brand-name">Quillmore Analytics</span>
  </div>

  <div class="intro">
    <h1 class="intro-title">DOLOR SIT AMET TELASDE</h1>
    <p class="intro-text">Consectetur adipisicing elit, sed do eiusmod tempor incididunt<br>ut dolore magna aliqua.<br>Ut enim ad minim veniam, quis nostrud ARGO.</p>
  </div>

  <!-- row 1 -->
  <a class="tile tile--link tile--red" href="#services" style="left:789.4px; top:44px;">
    <svg viewBox="0 0 60 60" fill="none" stroke="#fff" stroke-width="2.6" stroke-linecap="round" stroke-linejoin="round">
      <path d="M30 6a15 15 0 0 0-9 27c2 2 3 4 3 7h12c0-3 1-5 3-7a15 15 0 0 0-9-27z"/>
      <path d="M24 45h12M25 50h10M27 55h6M30 40V28l-4-4M30 28l4-4"/>
    </svg>
    <span>Services</span>
  </a>
  <div class="tile photo-lounge" style="left:975px; top:44px;" role="img" aria-label="Bright modern lounge with staircase and glass railing"></div>

  <!-- row 2 -->
  <div class="tile photo-terrace" style="left:47px; top:229.6px;" role="img" aria-label="Rooftop terrace at dusk with glowing furniture"></div>
  <a class="tile tile--link tile--red" href="#portfolio" style="left:232.6px; top:229.6px;">
    <svg viewBox="0 0 60 60" fill="none" stroke="#fff" stroke-width="2.6" stroke-linejoin="round">
      <rect x="6" y="6" width="48" height="48" rx="5"/>
      <rect x="13" y="13" width="34" height="34"/>
      <circle cx="36" cy="22" r="4"/>
      <path d="M13 42l11-12 9 9 5-5 9 9"/>
    </svg>
    <span>Portfolio</span>
  </a>
  <a class="tile tile--link tile--orange" href="#about" style="left:418.2px; top:229.6px;">
    <svg viewBox="0 0 60 60" fill="none" stroke="#fff" stroke-width="2.6" stroke-linejoin="round">
      <path d="M30 9C16 9 6 17 6 27c0 6 4 11 10 14l-3 10 11-7c2 .4 4 .6 6 .6 14 0 24-8 24-18S44 9 30 9z"/>
    </svg>
    <span>About us</span>
  </a>
  <div class="tile photo-dining" style="left:603.8px; top:229.6px;" role="img" aria-label="Wood-panelled dining room with angular table and chairs"></div>
  <div class="tile photo-sofa" style="left:789.4px; top:229.6px;" role="img" aria-label="Dark living room with black sofa and cushions"></div>
  <a class="tile tile--link tile--orange" href="#blog" style="left:975px; top:229.6px;">
    <svg viewBox="0 0 60 60" fill="none" stroke="#fff" stroke-width="2.6" stroke-linejoin="round">
      <path d="M6 12h40v36a4 4 0 0 0 4 4H10a4 4 0 0 1-4-4z"/>
      <path d="M46 20h8v28a4 4 0 0 1-8 0"/>
      <rect x="12" y="18" width="14" height="12"/>
      <path d="M31 19h9M31 25h9M31 30h9M12 36h28M12 42h28"/>
    </svg>
    <span>Blog</span>
  </a>

  <!-- row 3 -->
  <div class="tile photo-sunset" style="left:418.2px; top:415.2px;" role="img" aria-label="Curved glass living space overlooking a sunset"></div>
  <div class="tile photo-living" style="left:603.8px; top:415.2px;" role="img" aria-label="Grey sectional sofa with mustard cushions and floor lamp"></div>
  <a class="tile tile--link tile--red" href="#contact" style="left:789.4px; top:415.2px;">
    <svg viewBox="0 0 60 60" fill="none" stroke="#fff" stroke-width="2.6" stroke-linejoin="round">
      <path d="M54 6L4 28l14 6 36-28-26 32 4 16 8-12 10 6z"/>
      <path d="M18 34l4 16 10-12"/>
    </svg>
    <span>Contact</span>
  </a>
</header>

<nav class="main-nav">
  <a class="nav-item" href="#services">
    <svg viewBox="0 0 60 60" fill="none" stroke="#fff" stroke-width="3" stroke-linecap="round" stroke-linejoin="round"><path d="M30 6a15 15 0 0 0-9 27c2 2 3 4 3 7h12c0-3 1-5 3-7a15 15 0 0 0-9-27z"/><path d="M24 45h12M25 50h10M27 55h6"/></svg>
    <span>Services</span>
  </a>
  <a class="nav-item" href="#portfolio">
    <svg viewBox="0 0 60 60" fill="none" stroke="#fff" stroke-width="3" stroke-linejoin="round"><rect x="6" y="6" width="48" height="48" rx="5"/><rect x="13" y="13" width="34" height="34"/><circle cx="36" cy="22" r="4"/><path d="M13 42l11-12 9 9 5-5 9 9"/></svg>
    <span>Portfolio</span>
  </a>
  <a class="nav-item" href="#about">
    <svg viewBox="0 0 60 60" fill="none" stroke="#fff" stroke-width="3" stroke-linejoin="round"><path d="M30 9C16 9 6 17 6 27c0 6 4 11 10 14l-3 10 11-7c2 .4 4 .6 6 .6 14 0 24-8 24-18S44 9 30 9z"/></svg>
    <span>About us</span>
  </a>
  <a class="nav-item" href="#blog">
    <svg viewBox="0 0 60 60" fill="none" stroke="#fff" stroke-width="3" stroke-linejoin="round"><path d="M6 12h40v36a4 4 0 0 0 4 4H10a4 4 0 0 1-4-4z"/><path d="M46 20h8v28a4 4 0 0 1-8 0"/><rect x="12" y="18" width="14" height="12"/><path d="M31 19h9M31 25h9M12 36h28M12 42h28"/></svg>
    <span>Blog</span>
  </a>
  <a class="nav-item" href="#contact">
    <svg viewBox="0 0 60 60" fill="none" stroke="#fff" stroke-width="3" stroke-linejoin="round"><path d="M54 6L4 28l14 6 36-28-26 32 4 16 8-12 10 6z"/><path d="M18 34l4 16 10-12"/></svg>
    <span>Contact</span>
  </a>
</nav>

<section class="solutions">
  <h2 class="solutions-title">Advanced &amp; Secure Solutions</h2>
  <p class="solutions-lead">We perform either in-depth scientific research and analysis,<br>or very rapid-response evaluations,</p>
</section>

<div class="rule"></div>

<article class="capability" style="left:54px;">
  <svg viewBox="0 0 72 72" fill="none" stroke="#f0892a" stroke-width="3.4" stroke-linecap="round" stroke-linejoin="round">
    <path d="M50 8l14 14-36 36-18 6 6-18z"/>
    <path d="M44 14l14 14M16 46l10 10M40 18L22 36"/>
  </svg>
  <h3 class="capability-title">ADVICE</h3>
  <p class="capability-text">Lorem ipsum dolor sit amet, consectetur<br>adipisicing elit, tempor incididunt.</p>
</article>

<article class="capability" style="left:426px;">
  <svg viewBox="0 0 72 72" fill="none" stroke="#f0892a" stroke-width="3.4" stroke-linecap="round" stroke-linejoin="round">
    <path d="M26 14l16 16-16 26a8 8 0 0 0 6 10h0l26-16-16-16z" transform="rotate(-10 36 36)"/>
    <path d="M22 12l20 20"/>
    <circle cx="30" cy="48" r="3"/>
    <circle cx="40" cy="42" r="2"/>
    <circle cx="56" cy="10" r="4"/>
    <circle cx="60" cy="22" r="2"/>
  </svg>
  <h3 class="capability-title">DESIGN</h3>
  <p class="capability-text">Lorem ipsum dolor sit amet, consectetur<br>adipisicing elit, tempor incididunt.</p>
</article>

<article class="capability" style="left:794px;">
  <svg viewBox="0 0 72 72" fill="none" stroke="#f0892a" stroke-width="3.4" stroke-linejoin="round">
    <path d="M32 6h8l2 8 6 3 7-4 6 6-4 7 3 6 8 2v8l-8 2-3 6 4 7-6 6-7-4-6 3-2 8h-8l-2-8-6-3-7 4-6-6 4-7-3-6-8-2v-8l8-2 3-6-4-7 6-6 7 4 6-3z"/>
    <circle cx="36" cy="36" r="12"/>
    <circle cx="36" cy="36" r="5"/>
  </svg>
  <h3 class="capability-title">CONSTRUCTION</h3>
  <p class="capability-text">Lorem ipsum dolor sit amet, consectetur<br>adipisicing elit, tempor incididunt.</p>
</article>

</body>
</html>
```